Corvane Civic Modern, Sleek One Pager/Slick Sheet

Creative Brief: One-Pager Design for Corvane Civic
Project Overview:
We are seeking a highly skilled graphic designer to create a modern, sleek, and visually impactful one-pager (slick sheet) for Corvane Civic, a leading company in the defense and aerospace sector. This slick sheet will serve as a high-level marketing asset, designed to quickly capture attention and communicate Corvane Civic’s cutting-edge capabilities, technological expertise, and commitment to national security and innovation.
Key Objectives:
Establish a high-tech, sophisticated look and feel that aligns with the defense and aerospace industries.
Highlight Corvane Civic’s core competencies, key services, and differentiators with clear and concise messaging.
Ensure the design supports easy readability and quick scanning of critical information.
Incorporate strong visual hierarchy and premium, professional aesthetics.
Design Specifications:
Format: Single-page, print and digital distribution-ready (PDF format).
Layout Style: Clean, minimalist, and balanced with ample white space.
Typography: Modern, sans-serif fonts that convey innovation and strength.
Color Palette: Incorporate Corvane Civic’s brand colors (navy blue, steel gray, white, accents of metallic or deep reds if applicable).
Imagery: Use high-resolution imagery that reflects advanced technology, aerospace engineering, and national defense. Subtle technical graphics, schematics, or abstract patterns are acceptable to enhance visual interest without clutter.
Content Elements (To Be Provided):
Company Logo and Tagline
Key Capabilities and Service Offerings
Differentiators and Core Competencies
Contact Information
Visual Icons or Infographics for Quick Reference (if applicable)
Tone & Mood:
Professional, authoritative, and cutting-edge
Emphasizes trust, innovation, and mission-critical solutions
Appeals to government and defense industry stakeholders
Deliverables:
Final high-resolution print-ready PDF
Digital-friendly PDF optimized for email and web use
Source files (Adobe Illustrator, InDesign, or equivalent)
Target Market(s)
Defense/Aviation
Industry/Entity Type
Defense/Aviation
Look and feel

```html
<!DOCTYPE html>
<html lang="en">
<head>
<meta charset="utf-8">
<title>Corvane Civic – Slick Sheet</title>
<link href="https://fonts.googleapis.com/css2?family=Saira:wght@400;500&family=Albert+Sans:wght@400;500&display=swap" rel="stylesheet">
<style>
  :root {
    --navy: #0d2142;
    --navy-deep: #0b1d3d;
    --steel-light: #eeeff1;
    --steel-band: #e8e9ed;
    --ink: #111418;
    --white: #ffffff;
    --photo-top: #93a6c0;
    --photo-bottom: #b8b4aa;
  }
  * { margin: 0; padding: 0; box-sizing: border-box; }
  html, body { width: 927px; height: 1200px; overflow: hidden; background: var(--white); }
  .sheet {
    position: relative; width: 927px; height: 1200px; overflow: hidden;
    background: linear-gradient(135deg, #f3f4f6 0%, #fafbfc 45%, #eef0f3 100%);
    font-family: "Albert Sans", sans-serif; color: var(--ink);
  }
  .corner-shapes { position: absolute; left: 0; top: 0; }
  .header-panel {
    position: absolute; left: 202px; top: 66px; width: 523px; height: 109px;
    background: var(--steel-light); text-align: center;
  }
  .brand-name {
    margin-top: 24px; font-family: "Saira", sans-serif; font-weight: 500;
    font-size: 34px; letter-spacing: 5px; color: var(--ink); line-height: 1;
  }
  .brand-name::before {
    content: ""; display: inline-block; width: 14px; height: 14px;
    background: var(--ink); margin-right: 12px; vertical-align: 4px;
  }
  .tagline {
    margin-top: 18px; font-family: "Saira", sans-serif; font-size: 14px;
    color: var(--navy); letter-spacing: 0.2px;
  }
  .section-title {
    position: absolute; font-family: "Saira", sans-serif; font-weight: 400;
    font-size: 32px; line-height: 46px; color: var(--navy);
  }
  .section-title::after {
    content: ""; position: absolute; left: 2px; bottom: -14px;
    width: 52px; height: 2px; background: var(--navy);
  }
  .capabilities-title { left: 37px; top: 224px; }
  .differentiators-title { left: 503px; top: 225px; }
  .services-title { left: 565px; top: 705px; }

  .capability-list {
    position: absolute; left: 40px; top: 303px; width: 394px; list-style: none;
  }
  .capability-list li {
    position: relative; padding-left: 19px; font-size: 17.5px;
    line-height: 35px; margin-bottom: 12px;
  }
  .capability-list li::before {
    content: ""; position: absolute; left: 0; top: 15px;
    width: 5px; height: 5px; background: var(--navy);
  }
  .competency-list {
    position: absolute; left: 503px; top: 353px; list-style: none;
  }
  .competency-list li {
    display: flex; align-items: center; height: 44.8px;
    font-size: 17px; letter-spacing: 0.2px;
  }
  .competency-list svg { width: 15px; height: 15px; margin-right: 22px; flex-shrink: 0; }

  .lower-band {
    position: absolute; left: 0; top: 678px; width: 927px; height: 462px;
    background: linear-gradient(180deg, var(--steel-band) 0%, #e4e6eb 100%);
  }
  .photo-frame {
    position: absolute; left: 87px; top: 714px; width: 381px; height: 388px;
    border-radius: 14px; background: var(--navy);
  }
  .photo {
    position: absolute; left: 3px; top: 0; width: 378px; height: 384px;
    border-radius: 13px;
    background: linear-gradient(180deg, var(--photo-top) 0%, var(--photo-bottom) 100%);
  }
  .service-list { position: absolute; left: 566px; top: 782px; list-style: none; }
  .service-list li {
    display: flex; align-items: center; height: 65.5px; font-size: 16.5px; letter-spacing: 0.3px;
  }
  .service-icon {
    width: 41px; height: 41px; border-radius: 3px; background: var(--navy);
    display: flex; align-items: center; justify-content: center; margin-right: 21px;
  }
  .service-icon svg { width: 26px; height: 26px; }

  .footer {
    position: absolute; left: 0; top: 1140px; width: 927px; height: 60px;
    background: var(--navy-deep); color: var(--white);
  }
  .contact {
    position: absolute; top: 12px; display: flex; align-items: center;
    font-size: 16px; font-weight: 500; letter-spacing: 0.2px;
  }
  .contact-phone { left: 87px; }
  .contact-mail { left: 471px; }
  .contact-icon {
    width: 37px; height: 36px; background: var(--white); margin-right: 24px;
    display: flex; align-items: center; justify-content: center;
  }
  .contact-icon svg { width: 16px; height: 16px; }
</style>
</head>
<body>
<div class="sheet">
  <svg class="corner-shapes" width="927" height="280" viewBox="0 0 927 280" aria-hidden="true">
    <polygon points="0,21 245,24 282,66 202,66 0,264" fill="#0d2142"/>
    <polygon points="200,24 245,24 282,66 230,66" fill="#173563"/>
    <polygon points="927,20 682,24 645,66 725,66 927,264" fill="#0d2142"/>
    <polygon points="727,24 682,24 645,66 697,66" fill="#173563"/>
  </svg>

  <header class="header-panel">
    <div class="brand-name">CORVANE CIVIC</div>
    <p class="tagline">Mission-Critical Innovation. Unmatched Precision.</p>
  </header>

  <h2 class="section-title capabilities-title">Key Capabilities</h2>
  <ul class="capability-list">
    <li>Design, development, and integration of complex defense and aerospace systems for mission-critical performance.</li>
    <li>Deployment of AI, machine learning, and autonomous platforms for rapid situational awareness and decision-making.</li>
    <li>Expertise in spacecraft systems, satellite communications (SATCOM), telemetry, and orbital operations.</li>
  </ul>

  <h2 class="section-title differentiators-title">Differentiators &amp;<br>Core Competencies</h2>
  <ul class="competency-list">
    <li><svg viewBox="0 0 16 16"><circle cx="8" cy="8" r="8" fill="#0d2142"/><path d="M4.5 8.2l2.3 2.3 4.7-4.8" stroke="#fff" stroke-width="1.8" fill="none"/></svg>Mission-Focused Innovation</li>
    <li><svg viewBox="0 0 16 16"><circle cx="8" cy="8" r="8" fill="#0d2142"/><path d="M4.5 8.2l2.3 2.3 4.7-4.8" stroke="#fff" stroke-width="1.8" fill="none"/></svg>Defense-Grade Engineering Excellence</li>
    <li><svg viewBox="0 0 16 16"><circle cx="8" cy="8" r="8" fill="#0d2142"/><path d="M4.5 8.2l2.3 2.3 4.7-4.8" stroke="#fff" stroke-width="1.8" fill="none"/></svg>Agile &amp; Secure Development Processes</li>
    <li><svg viewBox="0 0 16 16"><circle cx="8" cy="8" r="8" fill="#0d2142"/><path d="M4.5 8.2l2.3 2.3 4.7-4.8" stroke="#fff" stroke-width="1.8" fill="none"/></svg>Top-Tier Federal Partnerships</li>
    <li><svg viewBox="0 0 16 16"><circle cx="8" cy="8" r="8" fill="#0d2142"/><path d="M4.5 8.2l2.3 2.3 4.7-4.8" stroke="#fff" stroke-width="1.8" fill="none"/></svg>End-to-End Systems Integration</li>
    <li><svg viewBox="0 0 16 16"><circle cx="8" cy="8" r="8" fill="#0d2142"/><path d="M4.5 8.2l2.3 2.3 4.7-4.8" stroke="#fff" stroke-width="1.8" fill="none"/></svg>Clearances &amp; Compliance</li>
  </ul>

  <section class="lower-band"></section>

  <div class="photo-frame">
    <div class="photo" role="img" aria-label="Photo of aircraft parked on an airfield apron beside a hangar"></div>
  </div>

  <h2 class="section-title services-title">Service Offerings</h2>
  <ul class="service-list">
    <li><span class="service-icon"><svg viewBox="0 0 26 26" fill="none" stroke="#fff" stroke-width="1.2"><circle cx="12" cy="14" r="10"/><circle cx="12" cy="14" r="6.5"/><circle cx="12" cy="14" r="3"/><path d="M12 14l9-9M18 5l3 0 0-3"/></svg></span>ISR Special Mission</li>
    <li><span class="service-icon"><svg viewBox="0 0 26 26" fill="none" stroke="#fff" stroke-width="1.2"><circle cx="7" cy="10" r="3.5"/><circle cx="13" cy="15" r="5"/><path d="M16.5 18.5l5 5M18 3v3M21 5l-2 2M15 5l2 2"/><circle cx="18" cy="10" r="2.5"/></svg></span>Research and Development</li>
    <li><span class="service-icon"><svg viewBox="0 0 26 26" fill="none" stroke="#fff" stroke-width="1.2"><circle cx="7" cy="5" r="2.2"/><path d="M7 8v7M4 11l3-2 4 2M5 22v-5M9 22v-5"/><circle cx="18" cy="7" r="3.5"/><rect x="13" y="14" width="10" height="8"/><path d="M15 20v-3M18 20v-4M21 20v-2"/></svg></span>CONUS Efforts</li>
    <li><span class="service-icon"><svg viewBox="0 0 26 26" fill="none" stroke="#fff" stroke-width="1.2"><circle cx="13" cy="8" r="3.5"/><circle cx="13" cy="8" r="1.2"/><path d="M3 12v6l5 5M23 12v6l-5 5M6 15l4 4M20 15l-4 4"/></svg></span>OCONUS Efforts</li>
    <li><span class="service-icon"><svg viewBox="0 0 26 26" fill="none" stroke="#fff" stroke-width="1.2"><path d="M20 4c1.5-1.5 3-1 2 1l-5 5 2 9-2 2-4-7-4 4v3l-2 1-1-4-4-1 1-2h3l4-4-7-4 2-2 9 2z"/><path d="M3 18l-2 2M5 21l-2 2"/></svg></span>Aviation Training</li>
  </ul>

  <footer class="footer">
    <div class="contact contact-phone">
      <span class="contact-icon"><svg viewBox="0 0 16 16"><path d="M3.5 1.5l2.5 2.5-1.5 2c1 2 2.5 3.5 4.5 4.5l2-1.5 2.5 2.5-1.5 2.5C7 14 2 9 1 3z" fill="#0d2142"/></svg></span>
      CALL US : (555) 204-7710
    </div>
    <div class="contact contact-mail">
      <span class="contact-icon"><svg viewBox="0 0 16 16" fill="none" stroke="#0d2142" stroke-width="1.3"><rect x="1" y="3" width="14" height="10"/><path d="M1 3l7 6 7-6M1 13l5-5M15 13l-5-5"/></svg></span>
      MAIL US : INFO@CORVANECIVIC.COM
    </div>
  </footer>
</div>
</body>
</html>
```